Lantern Sisters Ministries Logo/Business Card

Lantern Sisters are women full of God’s love and restorative grace, who have the desire to lead other women to embrace the beautiful creation that God intended them to be. Lantern Sisters walk together with other women alongside of God toward a life of healing, restoration and empowerment… through mentoring, spiritual guidance, temporary shelter, comprehensive care, and connections to a longer-term plan that leads to renewal and wholeness in Christ.

Lantern Sisters Ministries is an organization that embraces women and children whose lives have been affected by human trafficking, prison, foster care, homelessness, addictions, and other circumstances that prevent them from achieving their full potential in Christ Jesus. We believe that God has a unique plan and purpose for every individual. Through God’s transformational power and relationships with counselors, mentors, and others, anyone can break free from the chains and bondage of slavery, addictions and the strongholds of life.

We are just starting to brand our organization, and need both business cards and a logo. We do not have a logo yet, and would like design ideas. One of our young ladies (rescued from trafficking) has a vision of a logo with a crown with 3 ladies below/around it (representing healing, restoration, empowerment). Another lady has an idea of blending a crown, heart, and cross into the logo. We are open to creative suggestions.

Target Market(s)

Donations from churches, businesses, organizations and individuals with a passion for Trafficking and Justice

Industry/Entity Type

Business

Contact Information for Business Card

Lantern Sisters Ministries
sisters carrying light together toward hope, renewal and wholeness (tag line - italics)

Card 1:
Harriet Pellow, Director
555.218.3074
harriet@lanternsistersministries.org
www.lanternsistersministries.org (optional)

Card 2:
Rebecca Thorsby, Director
555.637.4152
becca@lanternsistersministries.org

```html
<!DOCTYPE html>
<html lang="en">
<head>
<meta charset="utf-8">
<title>Lantern Sisters Ministries – Business Card</title>
<link rel="stylesheet" href="https://fonts.googleapis.com/css2?family=Questrial&family=Cormorant+Garamond:ital,wght@1,600&display=swap">
<style>
  :root {
    --backdrop: #e9e9ea;
    --card-black: #1c1c1d;
    --card-black-edge: #2a2a2b;
    --card-white: #ffffff;
    --silver-light: #e6e6e6;
    --silver-dark: #8d8d8f;
    --brand-pink: #c8237f;
    --name-pink: #d63a92;
    --text-grey: #bdbdbd;
    --text-light: #e4e4e4;
    --brand-gold: #e8a92c;
  }
  html, body {
    margin: 0;
    width: 1200px;
    height: 900px;
    overflow: hidden;
    background: var(--backdrop);
  }
  .business-card {
    position: absolute;
    left: 100px;
    top: 164px;
    width: 1000px;
    height: 572px;
    border-radius: 44px;
    overflow: hidden;
    box-shadow: 0 18px 40px rgba(0,0,0,0.22);
  }
  .card-art { position: absolute; inset: 0; }
  .contact {
    position: absolute;
    left: 0;
    width: 560px;
    text-align: center;
    font-family: "Questrial", sans-serif;
    letter-spacing: 1px;
    white-space: nowrap;
  }
  .contact-name { top: 150px; font-size: 40px; color: var(--name-pink); }
  .contact-role { top: 202px; font-size: 22px; color: var(--text-grey); }
  .contact-phone { top: 280px; font-size: 38px; color: var(--name-pink); letter-spacing: 2px; }
  .contact-web { top: 372px; font-size: 22px; color: var(--text-light); }
  .contact-email { top: 402px; font-size: 22px; color: var(--text-light); }
  .brand-mark {
    position: absolute;
    left: 650px;
    top: 90px;
    width: 340px;
    text-align: center;
    font-family: "Questrial", sans-serif;
    color: var(--brand-pink);
    font-size: 44px;
    line-height: 1.15;
    letter-spacing: 2px;
    text-transform: uppercase;
  }
  .brand-dot {
    width: 120px;
    height: 120px;
    border-radius: 50%;
    background: var(--brand-gold);
    margin: 0 auto 28px;
  }
  .tagline {
    font-family: "Cormorant Garamond", serif;
    font-style: italic;
    font-weight: 600;
    font-size: 27px;
    letter-spacing: 1px;
  }
</style>
</head>
<body>
  <div class="business-card">
    <svg class="card-art" viewBox="0 0 1000 572" width="1000" height="572" aria-hidden="true">
      <defs>
        <linearGradient id="silver-band" x1="0" y1="0" x2="1" y2="0">
          <stop offset="0" stop-color="var(--silver-dark)"/>
          <stop offset="0.5" stop-color="var(--silver-light)"/>
          <stop offset="1" stop-color="var(--silver-dark)"/>
        </linearGradient>
        <linearGradient id="black-panel" x1="0" y1="0" x2="1" y2="1">
          <stop offset="0" stop-color="var(--card-black-edge)"/>
          <stop offset="1" stop-color="var(--card-black)"/>
        </linearGradient>
        <clipPath id="clip-black">
          <path d="M0 0 H600 C540 170 560 420 720 572 H0 Z"/>
        </clipPath>
        <clipPath id="clip-white">
          <path d="M600 0 H1000 V572 H720 C560 420 540 170 600 0 Z"/>
        </clipPath>
      </defs>
      <rect class="silver-band" x="0" y="0" width="1000" height="572" fill="url(#silver-band)"/>
      <path class="black-panel" d="M0 0 H600 C540 170 560 420 720 572 H0 Z" fill="url(#black-panel)"/>
      <path class="white-panel" d="M680 0 H1000 V572 H740 C600 420 600 160 680 0 Z" fill="var(--card-white)"/>
      <g clip-path="url(#clip-black)">
        <text class="tagline" x="60" y="535" textLength="880" fill="var(--card-white)">sisters carrying light together toward hope, renewal and wholeness</text>
      </g>
      <g clip-path="url(#clip-white)">
        <text class="tagline" x="60" y="535" textLength="880" fill="var(--card-black)">sisters carrying light together toward hope, renewal and wholeness</text>
      </g>
    </svg>

    <div class="contact contact-name">Harriet Pellow</div>
    <div class="contact contact-role">Director</div>
    <div class="contact contact-phone">555.218.3074</div>
    <div class="contact contact-web">www.lanternsistersministries.org</div>
    <div class="contact contact-email">harriet@lanternsistersministries.org</div>

    <div class="brand-mark">
      <div class="brand-dot"></div>
      Lantern Sisters<br>Ministries
    </div>
  </div>
</body>
</html>
```